A 500th Reformation Anniversary book

I am in need of a front and back cover design.
Front Cover:
The title is "KEEP IT SAFE -Edwin Harrow". It is an autobiography written as a biography. Harrow refers to this book's title in the respect that the book should be thrown into a bonfire and destroyed. Since this is a major part of the climax to the book, and since Harrow refers to the title and the cover photo, some type of fire photo is requested. In my working stage, I used a photograph that I had taken on our property.
Back Cover:
I would like a continuation in color from the front. The back will have the typical ISBN, etc. but also a short description of the book and two endorsements.
The final cover will need to be available for the following:
This book will have three formats. The book will be:
8.5" x 11" spiral bound - no spine
8.5" x 5.5" perfect bound
ebook
I do not have the exact spine width, but the page count for the perfect bound is 190.
I have confirmed that I will receive final copy that I can work with. I will need to add "School Edition" to the cover for the Spiral Bound.
I believe that's everything you need!
Thank you!
T.E.Voss

Target Market(s)

Middle School-Aged Children through Adults

Font styles to use
Sans Serif

Requirements
Must have
• See Project description plus...
• Title should be written such that it is clear that the 'Edwin Harrow' part of it is simply a byline to the words KEEP IT SAFE.

```html
<!DOCTYPE html>
<html lang="en">
<head>
<meta charset="utf-8">
<title>Keep It Safe — Front Cover</title>
<link rel="stylesheet" href="https://fonts.googleapis.com/css2?family=Oswald:wght@500;600;700&display=swap">
<style>
  :root {
    --page-bg: #ffffff;
    --cover-black: #040404;
    --ink-white: #ffffff;
    --flame-orange: #f0821a;
    --flame-gold: #ffc24a;
    --flame-yellow: #ffe27a;
    --ember-red: #9c2f0a;
    --paper-blue: #2a5a94;
    --paper-deep: #14294a;
    --paper-grey: #d4d6e2;
  }
  * { margin: 0; padding: 0; box-sizing: border-box; }
  html, body {
    width: 1200px;
    height: 1200px;
    overflow: hidden;
    background: var(--page-bg);
  }
  .canvas {
    position: relative;
    width: 1200px;
    height: 1200px;
  }
  .front-cover {
    position: absolute;
    left: 175px;
    top: 50px;
    width: 850px;
    height: 1100px;
    background: var(--cover-black);
    overflow: hidden;
    font-family: "Oswald", "Arial Narrow", sans-serif;
    color: var(--ink-white);
  }
  .fire-photo {
    position: absolute;
    inset: 0;
    background:
      /* pale burning pages */
      radial-gradient(ellipse 15% 7% at 30% 44%, rgba(220,222,234,0.9), transparent 75%),
      radial-gradient(ellipse 12% 8% at 50% 48%, rgba(212,214,226,0.75), transparent 75%),
      radial-gradient(ellipse 8% 7% at 18% 52%, rgba(212,214,226,0.5), transparent 75%),
      /* bright flame tongues */
      radial-gradient(ellipse 7% 16% at 68% 42%, rgba(255,226,122,0.85), transparent 72%),
      radial-gradient(ellipse 6% 14% at 58% 64%, rgba(255,194,74,0.8), transparent 72%),
      radial-gradient(ellipse 5% 10% at 78% 30%, rgba(255,194,74,0.6), transparent 72%),
      radial-gradient(ellipse 4% 5% at 66% 79%, rgba(255,226,122,0.8), transparent 75%),
      radial-gradient(ellipse 5% 9% at 20% 34%, rgba(240,130,26,0.55), transparent 72%),
      radial-gradient(ellipse 8% 10% at 38% 30%, rgba(240,130,26,0.35), transparent 72%),
      /* blue-lit crumpled paper bed */
      radial-gradient(ellipse 46% 14% at 44% 52%, rgba(42,90,148,0.9), transparent 78%),
      radial-gradient(ellipse 55% 20% at 48% 55%, rgba(20,41,74,0.9), transparent 80%),
      /* body of the fire */
      radial-gradient(ellipse 24% 36% at 66% 46%, rgba(240,130,26,0.75), transparent 72%),
      radial-gradient(ellipse 36% 46% at 62% 48%, rgba(156,47,10,0.55), transparent 76%),
      var(--cover-black);
  }
  .title {
    position: absolute;
    left: 130px;
    top: 58px;
    font-weight: 700;
    font-size: 132px;
    line-height: 1;
    letter-spacing: 1px;
    white-space: nowrap;
  }
  .byline {
    position: absolute;
    left: 310px;
    top: 222px;
    font-weight: 600;
    font-size: 54px;
    line-height: 1;
    white-space: nowrap;
  }
  .author {
    position: absolute;
    left: 330px;
    top: 855px;
    font-weight: 600;
    font-size: 74px;
    line-height: 1;
    letter-spacing: 1px;
    white-space: nowrap;
  }
</style>
</head>
<body>
  <main class="canvas">
    <section class="front-cover">
      <div class="fire-photo" role="img" aria-label="Photograph of printed book pages burning in a bonfire: pale pages on blue-lit crumpled paper with orange and gold flames rising against black"></div>
      <h1 class="title">KEEP IT SAFE</h1>
      <p class="byline">Edwin Harrow</p>
      <p class="author">T.E.Voss</p>
    </section>
  </main>
</body>
</html>
```